Fun, challenging, and inspirational guide for life change - written by a coach, therapist and founde

I need (1) cover design for a book titled:
"THE WANDERER'S TOOLKIT FOR MIND-SHIFTING IDEAS" - the surprisingly practical magic of believing and taking action

A 2ND COVER will be need for a companion ebook, titled:
"THE HEARTH LEDGER FOR PURPOSE AND CONTENTMENT - 3 steps to help unlock and unleash the unlimited you by loving your limitations

These books will be used to promote a larger suite of products and services devoted to empowering and inspiring a community of OVERCOMERS.

For reference check out www.brightquillpath.com

I've included some photos for visual reference points.

DESIGNS CONCEPTS:
CLEAN - A BLEND OF PAST AND PRESENT - MODERN AND THE SACRED) (...The Marlowe's Atlas meets

Target Market(s)

young and aspiring professionals and seasoned pros looking for life-changes due to feeling unfulfilled in their profession and relationships

Industry/Entity Type

Life Coaching

Font styles to use
Serif
Sans Serif

Requirements
Must have
• CREATIVITY - ORIGINALITY - WICKEDLY CLEAN DESIGN- AND IMPACTFUL TRANSLATION OF BRAND CONCEPT - COLOR AND PUNCH
Nice to have
• I included some photos as reference point - **PLEASE SEE THE PHOTOS FOR THE STAR-GAZERS DESIGNS** - I really like the feeling they provoke - I want to give the viewer a sense of the journey that can be taken when they dive into these books.
• Basically, riff off the design profiles and colors included in the STAR-GAZER covers.
• MUSTS INCLUDE -
• -ORIGINALITY
• - IMPACT
• - COLOR
• - ORIGINAL DESIGNS+
• +
Should not have
• STAY AWAY FROM...
• 1 OVERUSED AND TRENDY ICONS
• - ESOTERIC IMAGES
• - FLOWERY SCRIPTS
• - I AM REALLY LOOKING FOR A UPDATE OF THE TYPICAL SELF-HELP BOOK COVERS WHICH RELY TOO MUCH ON FLOWERY AND SACRED IMAGERY
• THANK YOU - feel free to unleash your creativity!

```html
<!DOCTYPE html>
<html lang="en">
<head>
<meta charset="utf-8">
<title>The Wanderer's Toolkit for Mind-Shifting Ideas — Cover</title>
<link rel="stylesheet" href="https://fonts.googleapis.com/css2?family=Cabin:wght@400;500&family=Lato:wght@700&display=swap">
<style>
  :root {
    --cover-top: #860a7c;
    --cover-mid: #5c0c4c;
    --cover-bottom: #2c0a19;
    --ink-light: #ffffff;
    --symbol-tone: #f6eef5;
  }
  html, body {
    margin: 0;
    padding: 0;
    width: 800px;
    height: 1200px;
    overflow: hidden;
    background: var(--cover-bottom);
  }
  .book-cover {
    position: relative;
    width: 800px;
    height: 1200px;
    overflow: hidden;
    background: linear-gradient(180deg, var(--cover-top) 0%, var(--cover-mid) 50%, var(--cover-bottom) 100%);
    color: var(--ink-light);
  }
  .book-title {
    position: absolute;
    top: 66px;
    left: 0;
    width: 800px;
    margin: 0;
    text-align: center;
    font-family: "Cabin", "Gill Sans", sans-serif;
    font-weight: 400;
    font-size: 64px;
    line-height: 82px;
    letter-spacing: 1px;
    text-transform: uppercase;
  }
  .book-title span { display: block; }
  .emblem-row {
    position: absolute;
    top: 500px;
    left: 0;
    width: 800px;
    height: 200px;
  }
  .book-subtitle {
    position: absolute;
    top: 938px;
    left: 0;
    width: 800px;
    margin: 0;
    text-align: center;
    font-family: "Lato", sans-serif;
    font-weight: 700;
    font-size: 24px;
    line-height: 34px;
    letter-spacing: 0.3px;
  }
  .book-subtitle span { display: block; }
</style>
</head>
<body>
  <main class="book-cover">
    <h1 class="book-title">
      <span>The Wanderer's</span>
      <span>Toolkit for</span>
      <span>Mind-Shifting</span>
      <span>Ideas</span>
    </h1>

    <svg class="emblem-row" viewBox="0 500 800 200" width="800" height="200">
      <g fill="none" stroke="var(--ink-light)" stroke-width="1.6" stroke-linejoin="miter">
        <polygon class="emblem-frame" points="215,510 110,690 320,690"/>
        <polygon class="emblem-frame" points="400,510 295,690 505,690"/>
        <polygon class="emblem-frame" points="585,510 480,690 690,690"/>
      </g>
      <circle cx="215" cy="630" r="34" fill="var(--symbol-tone)" role="img" aria-label="Symbol of a bird looking back over its shoulder"/>
      <circle cx="400" cy="628" r="34" fill="var(--symbol-tone)" role="img" aria-label="Symbol of falling water drops and ripples"/>
      <circle cx="588" cy="628" r="34" fill="var(--symbol-tone)" role="img" aria-label="Symbol of three joined spirals"/>
    </svg>

    <p class="book-subtitle">
      <span>11 beliefs to unlock and unleash your</span>
      <span>passion and purpose on the world</span>
    </p>
  </main>
</body>
</html>
```